Zielgruppe
IT Dienstleistungen, Hardware- u. Softwarevertrieb, Consulting, Sicherheitssysteme
Meine Zielgruppe sind Geschäftskunden (B2B) - Kleine bis mittelständische Unternehmen
Aufgabenstellung
Verschiedene Buttons, wie z.B. Partnernetzwerk, Wir über uns, Aktuelle Angebote, Zertifikate. Die Seite gibt kreativen Spielraum und ist an keinerlei Vorgabe gebunden - Innovatives und modernes Design sind willkommen (darf ruhig mal außergewöhlich sein). Logo ist vorhanden und sollte eingebaut werden (siehe Upload). Anregungen können ebenfalls der Landing Page entnommen werden. Zudem fände ich es gut, wenn einige bewegliche Bilder auf der Seite eingebaut würden und die rote Farbe des Hutes im Layout auftaucht (wenn möglich).

```html
<!DOCTYPE html>
<html lang="de">
<head>
<meta charset="utf-8">
<title>KORVAN-IT – Informationstechnik mit Stil</title>
<link href="https://fonts.googleapis.com/css2?family=Bebas+Neue&family=Fira+Sans:wght@300;400;500;600&display=swap" rel="stylesheet">
<style>
:root{
  --red:#e0161b;
  --ink:#1d1d1f;
  --slate:#3e4352;
  --slate-deep:#2f3441;
  --band:#ececec;
  --field:#efefef;
  --rule:#8a8a8a;
  --badge-blue:#1c8fd6;
  --badge-grey:#a4a6a8;
  --footer:#232325;
  --map:#e6e8e4;
}
*{box-sizing:border-box;margin:0;padding:0}
html,body{width:1200px;height:3175px;overflow:hidden}
body{position:relative;background:#fff;font-family:"Fira Sans",sans-serif;color:var(--ink)}
.abs{position:absolute}

/* header */
.site-header{left:0;top:0;width:1200px;height:112px;background:#fff}
.brand{left:110px;top:38px;display:flex;align-items:center;gap:10px;font-weight:600;font-size:22px;color:var(--ink)}
.brand-mark{width:14px;height:14px;background:var(--red)}
.main-nav{right:84px;top:40px;display:flex;gap:44px;font-weight:300;font-size:17px;color:var(--ink)}

/* hero */
.hero{left:0;top:112px;width:1200px;height:479px;background:linear-gradient(100deg,#1a2536 0%,#223348 40%,#3f6a7d 75%,#2a4558 100%)}
.hero-figure{left:135px;top:104px;width:340px;height:250px;border-radius:50%;background:radial-gradient(circle,#c9cdd2 0%,#8a929a 60%,rgba(138,146,154,0) 72%)}
.hero-title{left:568px;top:178px;font-family:"Bebas Neue",sans-serif;color:var(--red);font-size:70px;line-height:1}
.hero-sub{left:568px;top:248px;font-family:"Bebas Neue",sans-serif;color:#fff;font-size:54px;line-height:1;letter-spacing:.5px}

/* promise */
.promise-band{left:0;top:591px;width:1200px;height:470px;background:var(--band)}
.promise-card{left:217px;top:556px;width:774px;height:429px;background:#fff}
.section-title{position:absolute;left:0;width:100%;text-align:center;font-weight:500;font-size:34px}
.section-title span{display:inline-block;padding:0 6px 8px;border-bottom:3px solid currentColor}
.promise-card .section-title{top:38px}
.promise-item{position:absolute;top:159px;width:180px;text-align:center;font-weight:500;font-size:19px;line-height:1.3}
.icon-box{width:128px;height:128px;margin:0 auto 24px;border:2px solid var(--ink);border-radius:6px;position:relative;display:flex;align-items:center;justify-content:center}
.icon-box::after{content:"";position:absolute;left:12px;right:12px;bottom:10px;height:3px;background:#c9c9c9}

/* service */
.service{left:0;top:1061px;width:1200px;height:577px;background:linear-gradient(180deg,#474c59 0%,var(--slate) 55%,#3a4150 100%);color:#fff}
.service .section-title{top:60px}
.service-item{position:absolute;top:186px;width:156px;text-align:center;font-weight:500;font-size:25px}
.service-box{width:156px;height:246px;border:2px solid #fff;border-radius:8px;margin-bottom:24px;display:flex;flex-direction:column;align-items:center;padding-top:50px;gap:16px}
.step{width:58px;height:58px;border:2px solid #fff;border-radius:50%;font-size:28px;line-height:54px}

/* certificates */
.certs-title{left:157px;top:1700px;font-size:24px;font-weight:500;color:#555}
.certs-rule{left:284px;top:1718px;width:736px;height:2px;background:var(--rule)}
.badge{top:1768px;height:98px}

/* contact */
.contact{left:0;top:1955px;width:1200px;height:673px;background:linear-gradient(180deg,#444a58 0%,var(--slate-deep) 100%);color:#fff}
.contact .section-title{top:52px}
.contact-info{position:absolute;top:150px;width:300px;text-align:center;font-size:14px;line-height:1.35}
.contact-info svg{display:block;margin:0 auto 12px}
.contact-rule{left:160px;top:267px;width:861px;height:2px;background:#e8e8e8}
.field{position:absolute;background:var(--field);color:#6b6b6b;font-size:12px;font-weight:500;padding:14px 12px}
.send{left:890px;top:557px;width:133px;height:36px;background:var(--red);border:2px solid #fff;color:#fff;font-weight:500;font-size:17px;text-align:center;line-height:32px}

/* map & footer */
.map{left:0;top:2630px;width:1200px;height:477px;background:linear-gradient(160deg,#eceeea 0%,var(--map) 60%,#dfe4dc 100%)}
.site-footer{left:0;top:3107px;width:1200px;height:68px;background:var(--footer);color:#fff;font-size:11px;font-weight:500;text-align:center;line-height:68px}
</style>
</head>
<body>

<header class="abs site-header">
  <div class="abs brand"><span class="brand-mark"></span>KORVAN-IT</div>
  <nav class="abs main-nav">
    <span>Partnernetzwerk</span><span>Wir über uns</span><span>Aktuelle Angebote</span><span>Zertifikate</span>
  </nav>
</header>

<section class="abs hero" role="img" aria-label="Dunkles Büro-Foto mit Laptop und Maskottchen mit rotem Hut">
  <div class="abs hero-figure" role="img" aria-label="Maskottchen-Illustration mit rotem Hut"></div>
  <h1 class="abs hero-title">KORVAN-IT</h1>
  <p class="abs hero-sub">INFORMATIONSTECHNIK MIT STIL</p>
</section>

<div class="abs promise-band"></div>
<section class="abs promise-card">
  <h2 class="section-title"><span>Unser Versprechen</span></h2>
  <div class="promise-item" style="left:104px">
    <div class="icon-box">
      <svg width="56" height="56" viewBox="0 0 56 56" fill="none" stroke="#1d1d1f" stroke-width="2.5"><rect x="10" y="8" width="36" height="40" rx="4"/><path d="M19 28l7 7 12-14"/></svg>
    </div>Individuelle<br>IT-Lösung</div>
  <div class="promise-item" style="left:305px">
    <div class="icon-box">
      <svg width="64" height="64" viewBox="0 0 64 64" fill="none" stroke="#1d1d1f" stroke-width="2.5"><circle cx="32" cy="32" r="28"/><path d="M32 14v18h12"/><circle cx="32" cy="8" r="1.5" fill="#1d1d1f"/><circle cx="32" cy="56" r="1.5" fill="#1d1d1f"/><circle cx="8" cy="32" r="1.5" fill="#1d1d1f"/><circle cx="56" cy="32" r="1.5" fill="#1d1d1f"/></svg>
    </div>Lokale Partner</div>
  <div class="promise-item" style="left:505px">
    <div class="icon-box">
      <svg width="64" height="64" viewBox="0 0 64 64" fill="none" stroke="#1d1d1f" stroke-width="2.5"><circle cx="32" cy="24" r="16"/><circle cx="32" cy="24" r="9"/><path d="M22 36L14 54l9-3 4 8 5-14M42 36l8 18-9-3-4 8-5-14"/></svg>
    </div>Engagiert und<br>Qualifiziert</div>
</section>

<section class="abs service" role="img" aria-label="Abgedunkeltes Luftbild einer Kleinstadt im Tal">
  <h2 class="section-title"><span>Unser Service</span></h2>
  <div class="service-item" style="left:298px">
    <div class="service-box">
      <svg width="100" height="100" viewBox="0 0 100 100" fill="none" stroke="#fff" stroke-width="2.5"><rect x="22" y="22" width="56" height="56" rx="4"/><path d="M34 8v12M46 8v12M58 8v12M70 8v12M34 80v12M46 80v12M58 80v12M70 80v12M8 34h12M8 46h12M8 58h12M8 70h12M80 34h12M80 46h12M80 58h12M80 70h12"/></svg>
      <div class="step">1</div>
    </div>Hardware</div>
  <div class="service-item" style="left:524px">
    <div class="service-box">
      <svg width="100" height="100" viewBox="0 0 100 100" fill="none" stroke="#fff" stroke-width="2.5"><path d="M22 48a28 28 0 0 1 56 0z"/><circle cx="50" cy="36" r="6"/><rect x="18" y="48" width="64" height="16" rx="3"/><rect x="24" y="64" width="52" height="22" rx="3"/></svg>
      <div class="step">2</div>
    </div>Software</div>
  <div class="service-item" style="left:746px">
    <div class="service-box">
      <svg width="100" height="100" viewBox="0 0 100 100" fill="none" stroke="#fff" stroke-width="2.5"><path d="M50 6l36 12v26c0 24-16 40-36 48C30 84 14 68 14 44V18z"/><path d="M50 16l26 9v19c0 18-12 30-26 37-14-7-26-19-26-37V25z"/><path d="M36 62l30-30M42 70l28-28M32 52l24-24"/></svg>
      <div class="step">3</div>
    </div>Sicherheit</div>
</section>

<h2 class="abs certs-title">Zertifikate</h2>
<div class="abs certs-rule"></div>
<div class="abs badge" style="left:160px;width:183px;background:#f4f4f4;border-radius:6px"></div>
<div class="abs badge" style="left:355px;width:210px;background:var(--badge-grey);border-radius:6px"></div>
<div class="abs badge" style="left:578px;width:140px;background:var(--badge-blue)"></div>
<div class="abs badge" style="left:729px;width:140px;background:var(--badge-blue)"></div>
<div class="abs badge" style="left:879px;width:141px;background:var(--badge-blue)"></div>

<section class="abs contact" role="img" aria-label="Abgedunkeltes Luftbild einer Kleinstadt">
  <h2 class="section-title"><span>Kontakt</span></h2>
  <div class="contact-info" style="left:192px">
    <svg width="44" height="34" viewBox="0 0 44 34" fill="none" stroke="#fff" stroke-width="2.5"><rect x="2" y="2" width="40" height="30"/><path d="M2 2l20 18L42 2M2 32l15-15M42 32L27 17"/></svg>
    info@korvan-it.de</div>
  <div class="contact-info" style="left:666px">
    <svg width="30" height="42" viewBox="0 0 30 42" fill="#fff"><path d="M15 0C7 0 0 6.5 0 15c0 10 15 27 15 27s15-17 15-27C30 6.5 23 0 15 0zm0 21a6 6 0 1 1 0-12 6 6 0 0 1 0 12z"/></svg>
    Am Mühlbach 12, 59900 Talheim<br>Deutschland</div>
  <div class="abs contact-rule"></div>
  <div class="field" style="left:158px;top:317px;width:274px;height:46px">Ihre Name</div>
  <div class="field" style="left:158px;top:377px;width:274px;height:46px">Ihre E-maile addresse</div>
  <div class="field" style="left:158px;top:436px;width:274px;height:46px">Ihre Telefonnr</div>
  <div class="field" style="left:158px;top:494px;width:274px;height:46px">Suburb</div>
  <div class="field" style="left:454px;top:317px;width:567px;height:46px">Ihre Subjec</div>
  <div class="field" style="left:454px;top:376px;width:567px;height:164px">Ihre Nachricht</div>
  <div class="abs send">Senden</div>
</section>

<div class="abs map" role="img" aria-label="Straßenkarte mit Firmenstandort"></div>

<footer class="abs site-footer">Copyright 2017 KORVAN-IT. All Rights Reserved | Terms and Conditions</footer>

</body>
</html>
```